New tech executive consulting company needs professionally branded document templates

We are a new business selling fractional board advisory and go-to-market consulting services into the Technology space. Partwise Helm are experts in providing high-quality executive-level leaders on a part-time basis to tech companies in need of their expertise. We work closely with clients to understand their business needs, challenges, and goals, and provides customised solutions to help them succeed. Due to our audience we need the design to have a high quality, executive look and feel.

Our first website is live and can be found at partwisehelm.tech. We also already have a logo which I've uploaded. Our brand is clean and uses orange to give it colour and an identity that stands out.

We need some document master templates created so we can create our own presentations (Google Slides & Powerpoint), PDF documents, and Word templates, and ideally also a LinkedIn banner.

```html
<!DOCTYPE html>
<html lang="en">
<head>
<meta charset="utf-8">
<title>Partwise Helm – Presentation Templates</title>
<link rel="stylesheet" href="https://fonts.googleapis.com/css2?family=Bebas+Neue&family=Montserrat:wght@400;500;600;700;800&display=swap">
<style>
:root{
  --navy:#28313d;
  --orange:#ee8a4b;
  --board:#d1d2d4;
  --white:#ffffff;
  --ink:#1f242b;
  --grid:#e3e5e8;
}
*{box-sizing:border-box;margin:0;padding:0}
html,body{width:777px;height:1200px;overflow:hidden;background:var(--board)}
body{font-family:"Montserrat",sans-serif;color:var(--ink)}
.board{position:relative;width:777px;height:1200px}
.slide{position:absolute;width:278px;height:173px;background:var(--white);overflow:hidden;box-shadow:0 6px 6px -4px rgba(0,0,0,.35)}
.slide.dark{background:var(--navy)}
.col-l{left:88px}.col-r{left:412px}
.row-1{top:105px}.row-2{top:308px}.row-3{top:507px}.row-4{top:707px}.row-5{top:907px}
.shape{position:absolute;inset:0;width:278px;height:173px}
.abs{position:absolute}
.brand{font-weight:800;letter-spacing:.6px;line-height:1.15;text-align:center;color:var(--navy)}
.dark .brand{color:var(--white)}
.brand-lg{font-size:8px;left:13px;top:16px}
.brand-foot{font-size:3.4px;left:10px;top:162px;letter-spacing:.2px}
.title{font-family:"Bebas Neue",sans-serif;font-size:22px;line-height:.92;left:13px;top:62px;color:var(--navy)}
.dark .title{color:var(--white)}
.title .accent,.accent{color:var(--orange)}
.subtitle{left:13px;top:104px;font-size:5.6px;font-weight:500}
.pill{background:var(--orange);color:var(--white);font-size:4.6px;border-radius:5px;padding:1.6px 5px;left:13px;top:119px}
.heading{font-family:"Bebas Neue",sans-serif;font-size:12.5px;color:var(--orange);left:8px;top:7px;letter-spacing:.2px}
.body{font-size:4.1px;line-height:7.8px;text-align:justify}
.small{font-size:3.2px;line-height:3.7px}
.item-title{font-size:5.5px;font-weight:500;color:var(--orange)}
.icon-circle{width:19px;height:19px;border-radius:50%;background:var(--orange)}
.photo{position:absolute}
.table{position:absolute;left:10px;top:47px;width:257px;font-size:3.5px}
.tr{position:absolute;left:5px;width:247px;height:11px;border-bottom:.5px solid #c9ccd0;display:flex;align-items:center}
.tr span{position:absolute;text-align:center;width:40px}
.tr span.lab{text-align:left;left:0;width:80px}
.thanks{font-family:"Bebas Neue",sans-serif;font-size:34px;line-height:.9;color:var(--white);left:19px;top:53px}
.contact{left:19px;top:124px;font-size:5.6px;line-height:10px;color:var(--white)}
.name{font-size:5.6px;font-weight:500;text-align:center}
</style>
</head>
<body>
<main class="board">

<!-- Cover, light -->
<section class="slide col-l row-1">
  <svg class="shape" viewBox="0 0 278 173">
    <defs><linearGradient id="photoNavy" x1="0" y1="0" x2="1" y2="1"><stop offset="0" stop-color="#2f3a47"/><stop offset="1" stop-color="#141b22"/></linearGradient></defs>
    <path d="M133,0 C122,40 142,60 138,78 C128,112 150,148 180,155" fill="none" stroke="var(--orange)" stroke-width=".8"/>
    <path role="img" aria-label="Photo of a smiling executive presenting in a meeting room" d="M140,0 C130,40 150,60 145,78 C135,112 160,150 200,173 L278,173 L278,0 Z" fill="url(#photoNavy)"/>
  </svg>
  <div class="abs brand brand-lg">PARTWISE<br>HELM</div>
  <h1 class="abs title">Presentation<br><span class="accent">Title Goeshere</span></h1>
  <p class="abs subtitle">Subtitle of Presentation Goes Here</p>
  <p class="abs pill">www.partwisehelm.tech</p>
</section>

<!-- Cover, dark -->
<section class="slide dark col-r row-1">
  <svg class="shape" viewBox="0 0 278 173">
    <defs><linearGradient id="photoOrange" x1="0" y1="0" x2="1" y2="1"><stop offset="0" stop-color="#d98a4e"/><stop offset=".6" stop-color="#9a5a33"/><stop offset="1" stop-color="#c77a45"/></linearGradient></defs>
    <path d="M133,0 C122,40 142,60 138,78 C128,112 150,148 180,155" fill="none" stroke="var(--orange)" stroke-width=".8"/>
    <path role="img" aria-label="Photo of a smiling executive presenting in a meeting room" d="M140,0 C130,40 150,60 145,78 C135,112 160,150 200,173 L278,173 L278,0 Z" fill="url(#photoOrange)"/>
  </svg>
  <div class="abs brand brand-lg">PARTWISE<br>HELM</div>
  <h1 class="abs title">Presentation<br><span class="accent">Title Goeshere</span></h1>
  <p class="abs pill">www.partwisehelm.tech</p>
</section>

<!-- Text slide -->
<section class="slide col-l row-2">
  <svg class="shape" viewBox="0 0 278 173">
    <path d="M93,0 H278 V22 H116 C102,22 101,0 93,0 Z" fill="var(--navy)"/>
    <rect x="40" y="163" width="238" height="3" fill="var(--orange)"/>
  </svg>
  <h2 class="abs heading">Heading Goes Here</h2>
  <div class="abs body" style="left:8px;top:47px;width:262px">
    <p>Lorem ipsum dolor sit amet, consectetuer adipiscing elit, sed diam nonummy nibh euismod tincidunt ut laoreet dolore magna aliquam erat volutpat. Ut wisi enim ad minim veniam, quis nostrud exerci tation ullamcorper suscipit lobortis nisl ut aliquip ex ea commodo consequat. Duis autem vel eum iriure dolor in hendrerit in vulputate velit esse molestie consequat, vel illum dolore eu feugiat nulla facilisis at vero eros et accumsan et iusto odio dignissim qui blandit praesent luptatum zzril delenit augue duis dolore te feugait nulla facilisi.</p>
    <p style="margin-top:7.8px">Lorem ipsum dolor sit amet, cons ectetuer adipiscing elit, sed diam nonummy nibh euismod tincidunt ut laoreet dolore magna aliquam erat volutpat. Ut wisi enim ad minim veniam, quis nostrud exerci tation ullamcorper suscipit lobortis nisl ut aliquip ex ea commodo consequat.</p>
  </div>
  <div class="abs brand brand-foot">PARTWISE<br>HELM</div>
</section>

<!-- Image + band slide -->
<section class="slide col-r row-2">
  <svg class="shape" viewBox="0 0 278 173">
    <path d="M93,0 H278 V22 H116 C102,22 101,0 93,0 Z" fill="var(--navy)"/>
    <rect x="100" y="58" width="178" height="79" fill="var(--navy)"/>
    <defs><linearGradient id="officeTone" x1="0" y1="0" x2="1" y2="0"><stop offset="0" stop-color="#8fa3b0"/><stop offset=".5" stop-color="#cfd6da"/><stop offset="1" stop-color="#6c7680"/></linearGradient></defs>
    <path role="img" aria-label="Photo of an executive leading a meeting in a bright office" d="M54,58 H110 L100,137 H54 A39.5,39.5 0 0 1 54,58 Z" fill="url(#officeTone)"/>
    <rect x="40" y="163" width="238" height="3" fill="var(--orange)"/>
  </svg>
  <h2 class="abs heading">Heading Goes Here</h2>
  <div class="abs" style="left:111px;top:65px;width:150px;color:var(--white)">
    <p style="font-family:'Bebas Neue',sans-serif;font-size:6.5px;color:var(--orange)">You Want:</p>
    <p class="small" style="font-size:3.3px;line-height:6.5px;text-align:justify">Lorem ipsum dolor sit amet, consectetuer adipiscing elit, sed diam nonummy nibh euismod tincidunt ut laoreet dolore magna aliquam erat volutpat. Ut lobortis nisl ut aliquip ex ea commodo consequat. Duis autem vel eum iriure dolor hendrerit in vulputate velit</p>
    <p class="small" style="font-size:3.3px;line-height:6.5px;text-align:justify;margin-top:6px">esse molestie consequat, vel illum dolore eu feugiat nulla facilisis at vero eros et accumsan et iusto odio dignissim qui blandit praesent luptatum zzril delenit augue duis dolore te feugait nulla facilisi.</p>
  </div>
  <div class="abs brand brand-foot">PARTWISE<br>HELM</div>
</section>

<!-- Four features -->
<section class="slide col-l row-3">
  <svg class="shape" viewBox="0 0 278 173">
    <path d="M93,0 H278 V22 H116 C102,22 101,0 93,0 Z" fill="var(--navy)"/>
    <g fill="var(--white)">
      <g transform="translate(22,72)"><circle cx="0" cy="-3" r="2.4"/><path d="M-4,5 V1.5 Q0,-1 4,1.5 V5 Z"/></g>
      <g transform="translate(152,72)"><circle cx="0" cy="-3" r="2.4"/><path d="M-4,5 V1.5 Q0,-1 4,1.5 V5 Z"/></g>
      <g transform="translate(22,116)"><circle cx="0" cy="-3" r="2.4"/><path d="M-4,5 V1.5 Q0,-1 4,1.5 V5 Z"/></g>
      <g transform="translate(152,116)"><circle cx="0" cy="-3" r="2.4"/><path d="M-4,5 V1.5 Q0,-1 4,1.5 V5 Z"/></g>
    </g>
    <g stroke="var(--ink)" stroke-width=".6"><line x1="36" y1="58" x2="36" y2="86"/><line x1="166" y1="58" x2="166" y2="86"/><line x1="36" y1="103" x2="36" y2="130"/><line x1="166" y1="103" x2="166" y2="130"/></g>
    <rect x="40" y="163" width="238" height="3" fill="var(--orange)"/>
  </svg>
  <div class="abs icon-circle" style="left:12px;top:62px;z-index:-0"></div>
  <h2 class="abs heading">Heading Goes Here</h2>
  <div class="abs" style="left:41px;top:61px;width:94px"><p class="item-title">Title Goes Here</p><p class="small" style="text-align:justify">Lorem ipsum dolor sit amet, consectetuer adipiscing elit, sed diam nonummy nibh euismod tincidunt ut laoreet dolore magna aliquam erat volutpat. Ut wisi enim ad minim veniam, quis nostrud exerci tation ullamcorper suscipit lobortis nisl ut</p></div>
  <div class="abs" style="left:171px;top:61px;width:94px"><p class="item-title">Title Goes Here</p><p class="small" style="text-align:justify">Lorem ipsum dolor sit amet, consectetuer adipiscing elit, sed diam nonummy nibh euismod tincidunt ut laoreet dolore magna aliquam erat volutpat. Ut wisi enim ad minim veniam, quis nostrud exerci tation ullamcorper suscipit lobortis nisl ut</p></div>
  <div class="abs" style="left:41px;top:105px;width:94px"><p class="item-title">Title Goes Here</p><p class="small" style="text-align:justify">Lorem ipsum dolor sit amet, consectetuer adipiscing elit, sed diam nonummy nibh euismod tincidunt ut laoreet dolore magna aliquam erat volutpat. Ut wisi enim ad minim veniam, quis nostrud exerci tation ullamcorper suscipit lobortis nisl ut</p></div>
  <div class="abs" style="left:171px;top:105px;width:94px"><p class="item-title">Title Goes Here</p><p class="small" style="text-align:justify">Lorem ipsum dolor sit amet, consectetuer adipiscing elit, sed diam nonummy nibh euismod tincidunt ut laoreet dolore magna aliquam erat volutpat. Ut wisi enim ad minim veniam, quis nostrud exerci tation ullamcorper suscipit lobortis nisl ut</p></div>
  <div class="abs brand brand-foot">PARTWISE<br>HELM</div>
</section>

<!-- Chart slide -->
<section class="slide col-r row-3">
  <svg class="shape" viewBox="0 0 278 173">
    <path d="M93,0 H278 V22 H116 C102,22 101,0 93,0 Z" fill="var(--navy)"/>
    <g stroke="var(--grid)" stroke-width=".4">
      <line x1="10" y1="50" x2="155" y2="50"/><line x1="10" y1="58" x2="155" y2="58"/><line x1="10" y1="66" x2="155" y2="66"/><line x1="10" y1="74" x2="155" y2="74"/><line x1="10" y1="82" x2="155" y2="82"/><line x1="10" y1="90" x2="155" y2="90"/><line x1="10" y1="98" x2="155" y2="98"/><line x1="10" y1="106" x2="155" y2="106"/>
      <line x1="34" y1="46" x2="34" y2="114"/><line x1="58" y1="46" x2="58" y2="114"/><line x1="82" y1="46" x2="82" y2="114"/><line x1="106" y1="46" x2="106" y2="114"/><line x1="130" y1="46" x2="130" y2="114"/><line x1="154" y1="46" x2="154" y2="114"/>
    </g>
    <g stroke="#9aa0a6" stroke-width=".5"><line x1="10" y1="46" x2="10" y2="114"/><line x1="10" y1="114" x2="158" y2="114"/></g>
    <circle cx="10" cy="45" r="1.4" fill="#b8bcc0"/><circle cx="159" cy="114" r="1.4" fill="#b8bcc0"/>
    <g font-family="Montserrat,sans-serif" font-size="1.6" fill="#555"><text x="6" y="51">40</text><text x="6" y="67">30</text><text x="6" y="83">20</text><text x="6" y="99">10</text><text x="8" y="117">0</text><text x="33" y="117">10</text><text x="57" y="117">30</text><text x="81" y="117">50</text><text x="105" y="117">70</text><text x="129" y="117">90</text></g>
    <polyline points="34,114 40,74 58,66 82,98 88,114 94,114 106,74 118,90 130,82 142,114" fill="none" stroke="var(--orange)" stroke-width=".6"/>
    <g fill="var(--orange)"><circle cx="34" cy="114" r=".9"/><circle cx="40" cy="74" r=".9"/><circle cx="58" cy="66" r=".9"/><circle cx="82" cy="98" r=".9"/><circle cx="88" cy="114" r=".9"/><circle cx="94" cy="114" r=".9"/><circle cx="106" cy="74" r=".9"/><circle cx="118" cy="90" r=".9"/><circle cx="130" cy="82" r=".9"/><circle cx="142" cy="114" r=".9"/></g>
    <polyline points="24,114 34,90 43,102 58,98 82,114" fill="none" stroke="var(--ink)" stroke-width=".6"/>
    <g fill="var(--ink)"><circle cx="24" cy="114" r=".9"/><circle cx="34" cy="90" r=".9"/><circle cx="43" cy="102" r=".9"/><circle cx="58" cy="98" r=".9"/><circle cx="82" cy="114" r=".9"/></g>
    <rect x="40" y="163" width="238" height="3" fill="var(--orange)"/>
  </svg>
  <h2 class="abs heading">Heading Goes Here</h2>
  <div class="abs" style="left:173px;top:44px;width:86px">
    <p class="item-title" style="font-size:5px">Title Goes Here</p><p class="small" style="font-size:2.8px;line-height:3.3px;text-align:justify">Lorem ipsum dolor sit amet, consectetuer adipiscing elit, sed diam nonummy nibh euismod tincidunt ut laoreet dolore magna aliquam erat volutpat. Ut wisi enim ad minim veniam, quis nostrud exerci tation ullamcorper suscipit lobortis nisl ut</p>
    <p class="item-title" style="font-size:5px;margin-top:5px">Title Goes Here</p><p class="small" style="font-size:2.8px;line-height:3.3px;text-align:justify">Lorem ipsum dolor sit amet, consectetuer adipiscing elit, sed diam nonummy nibh euismod tincidunt ut laoreet dolore magna aliquam erat volutpat. Ut wisi enim ad minim veniam, quis nostrud exerci tation ullamcorper suscipit lobortis nisl ut</p>
    <p class="item-title" style="font-size:5px;margin-top:5px">Title Goes Here</p><p class="small" style="font-size:2.8px;line-height:3.3px;text-align:justify">Lorem ipsum dolor sit amet, consectetuer adipiscing elit, sed diam nonummy nibh euismod tincidunt ut laoreet dolore magna aliquam erat volutpat. Ut wisi enim ad minim veniam, quis nostrud exerci tation ullamcorper suscipit lobortis nisl ut</p>
  </div>
  <div class="abs" style="left:10px;top:124px;width:255px">
    <p class="item-title" style="font-size:5px">Title Goes Here</p>
    <p class="small" style="font-size:2.8px;line-height:3.3px">Lorem ipsum dolor sit amet, consectetuer adipiscing elit, sed diam nonummy nibh euismod tincidunt ut laoreet dolore magna aliquam erat volutpat. Ut wisi enim ad minim veniam, quis nostrud exerci tation ullamcorper suscipit lobortis nisl ut aliquip ex ea commodo consequat. Duis autem vel eum iriure dolor in hendrerit in vulputate velit esse molestie.</p>
    <p class="small" style="font-size:2.8px;line-height:3.3px;margin-top:3px">Lorem ipsum dolor sit amet, consectetuer adipiscing elit, sed diam nonummy nibh euismod tincidunt ut laoreet dolore magna aliquam erat volutpat. Ut wisi enim ad minim veniam.</p>
  </div>
  <div class="abs brand brand-foot">PARTWISE<br>HELM</div>
</section>

<!-- Table slide -->
<section class="slide col-l row-4">
  <svg class="shape" viewBox="0 0 278 173">
    <path d="M93,0 H278 V22 H116 C102,22 101,0 93,0 Z" fill="var(--navy)"/>
    <rect x="10" y="48" width="257" height="13" rx="6.5" fill="var(--navy)"/>
    <path d="M90,48 V46 Q90,45 92,45 H131 Q133,45 133,47 V61 H90 Z" fill="var(--orange)"/>
    <rect x="90" y="45" width="43" height="96" rx="3" fill="none" stroke="var(--orange)" stroke-width=".7"/>
    <rect x="40" y="163" width="238" height="3" fill="var(--orange)"/>
  </svg>
  <h2 class="abs heading">Heading Goes Here</h2>
  <div class="table">
    <div class="tr" style="top:1px;height:13px;border:none;color:var(--white)"><span class="lab" style="left:2px">Heading Goes Here</span><span style="left:80px;font-size:3.2px;line-height:3.8px">Heading<br>Goes Here</span><span style="left:123px;font-size:3.2px;line-height:3.8px">Heading<br>Goes Here</span><span style="left:166px;font-size:3.2px;line-height:3.8px">Heading<br>Goes Here</span><span style="left:209px;font-size:3.2px;line-height:3.8px">Heading<br>Goes Here</span></div>
    <div class="tr" style="top:16px"><span class="lab">Lorem Ipsum Goes Here</span><span style="left:80px">23</span><span style="left:123px">12</span><span style="left:166px">78</span><span style="left:209px">12</span></div>
    <div class="tr" style="top:27px"><span class="lab">Lorem Ipsum Goes Here</span><span style="left:80px">45</span><span style="left:123px">56</span><span style="left:166px">12</span><span style="left:209px">56</span></div>
    <div class="tr" style="top:38px"><span class="lab">Lorem Ipsum Goes Here</span><span style="left:80px">78</span><span style="left:123px">76</span><span style="left:166px">34</span><span style="left:209px">76</span></div>
    <div class="tr" style="top:49px"><span class="lab">Lorem Ipsum Goes Here</span><span style="left:80px">22</span><span style="left:123px">12</span><span style="left:166px">55</span><span style="left:209px">12</span></div>
    <div class="tr" style="top:60px"><span class="lab">Lorem Ipsum Goes Here</span><span style="left:80px">34</span><span style="left:123px">66</span><span style="left:166px">45</span><span style="left:209px">66</span></div>
    <div class="tr" style="top:71px"><span class="lab">Lorem Ipsum Goes Here</span><span style="left:80px">67</span><span style="left:123px">47</span><span style="left:166px">78</span><span style="left:209px">47</span></div>
    <div class="tr" style="top:82px"><span class="lab">Lorem Ipsum Goes Here</span><span style="left:80px">87</span><span style="left:123px">67</span><span style="left:166px">12</span><span style="left:209px">67</span></div>
  </div>
  <div class="abs brand brand-foot">PARTWISE<br>HELM</div>
</section>

<!-- Three columns with images -->
<section class="slide col-r row-4">
  <svg class="shape" viewBox="0 0 278 173">
    <path d="M93,0 H278 V22 H116 C102,22 101,0 93,0 Z" fill="var(--navy)"/>
    <defs><linearGradient id="teamTone" x1="0" y1="0" x2="1" y2="1"><stop offset="0" stop-color="#d9dadc"/><stop offset="1" stop-color="#3d4046"/></linearGradient>
    <linearGradient id="techTone" x1="0" y1="0" x2="1" y2="1"><stop offset="0" stop-color="#a9d3ef"/><stop offset="1" stop-color="#1f4e7a"/></linearGradient>
    <linearGradient id="deskTone" x1="0" y1="0" x2="1" y2="1"><stop offset="0" stop-color="#8eb4d6"/><stop offset="1" stop-color="#e9eef3"/></linearGradient></defs>
    <rect role="img" aria-label="Photo of a team working around a table" x="14" y="74" width="75" height="36" rx="18" fill="url(#teamTone)"/>
    <rect role="img" aria-label="Photo of hands using a tablet with digital overlay" x="102" y="74" width="75" height="36" rx="18" fill="url(#techTone)"/>
    <rect role="img" aria-label="Photo of colleagues reviewing charts at a desk" x="191" y="74" width="75" height="36" rx="18" fill="url(#deskTone)"/>
    <g fill="var(--orange)"><circle cx="16" cy="130" r=".9"/><circle cx="104" cy="130" r=".9"/><circle cx="193" cy="130" r=".9"/></g>
    <rect x="40" y="163" width="238" height="3" fill="var(--orange)"/>
  </svg>
  <h2 class="abs heading">Heading Goes Here</h2>
  <p class="abs small" style="left:10px;top:51px;width:258px;font-size:3.4px;line-height:4.1px;text-align:justify">Northfield Ore Limited (ASX: NFO) is an Australian exploration company with brownfield metals projects in North America. The Company's strategy is to develop a portfolio of projects that support the green economy through the discovery and delivery of commodities that promote electrification and decarbonisation. We seek to maximise shareholder value through the acquisition, discovery, and advancement of high quality precious, base, and strategic metal projects in North America.</p>
  <p class="abs item-title" style="left:14px;top:114px;width:75px;text-align:center">Heading Goes Here</p>
  <p class="abs item-title" style="left:102px;top:114px;width:75px;text-align:center">Heading Goes Here</p>
  <p class="abs item-title" style="left:191px;top:114px;width:75px;text-align:center">Heading Goes Here</p>
  <p class="abs small" style="left:22px;top:128px;width:60px;font-size:3.3px">Lorem ipsum dolar sit amet, consectetur adipising edit. Vivamus eu dui ex.</p>
  <p class="abs small" style="left:110px;top:128px;width:60px;font-size:3.3px">Lorem ipsum dolar sit amet, consectetur adipising edit. Vivamus eu dui ex.</p>
  <p class="abs small" style="left:199px;top:128px;width:60px;font-size:3.3px">Lorem ipsum dolar sit amet, consectetur adipising edit. Vivamus eu dui ex.</p>
  <div class="abs brand brand-foot">PARTWISE<br>HELM</div>
</section>

<!-- Team slide -->
<section class="slide col-l row-5">
  <svg class="shape" viewBox="0 0 278 173">
    <path d="M93,0 H278 V22 H116 C102,22 101,0 93,0 Z" fill="var(--navy)"/>
    <g fill="var(--orange)"><circle cx="45" cy="77" r="12.5"/><circle cx="107" cy="77" r="12.5"/><circle cx="170" cy="77" r="12.5"/><circle cx="232" cy="77" r="12.5"/></g>
    <g fill="var(--white)">
      <g transform="translate(45,77)"><circle cy="-2" r="2"/><path d="M-3.5,4 V2 Q0,0 3.5,2 V4 Z"/></g>
      <g transform="translate(107,77)"><circle cy="-2" r="2"/><path d="M-3.5,4 V2 Q0,0 3.5,2 V4 Z"/></g>
      <g transform="translate(170,77)"><circle cy="-2" r="2"/><path d="M-3.5,4 V2 Q0,0 3.5,2 V4 Z"/></g>
      <g transform="translate(232,77)"><circle cy="-2" r="2"/><path d="M-3.5,4 V2 Q0,0 3.5,2 V4 Z"/></g>
    </g>
    <rect x="40" y="163" width="238" height="3" fill="var(--orange)"/>
  </svg>
  <h2 class="abs heading">Heading Goes Here</h2>
  <p class="abs small" style="left:13px;top:41px;width:252px;font-size:3.2px;text-align:center">Lorem ipsum dolor sit amet, consectetuer adipiscing elit, sed diam nonummy nibh euismod tincidunt ut laoreet dolore magna aliquam erat volutpat. Ut wisi enim ad minim veniam, quis nostrud exerci tation ullamcorper suscipit lobortis<br>Lorem ipsum dolor sit amet, consectetuer adipiscing elit, sed diam nonummy nibh euismod tincidunt ut laoreet dolore magna aliquam erat volutpat. Ut wisi enim ad minim veniam, quis nostrud exerci tation ullamcorper suscipit lobortis</p>
  <div class="abs" style="left:23px;top:96px;width:45px"><p class="name">Name Here</p><p class="small" style="font-size:3.2px;text-align:justify">Lorem ipsum dolor sit amet, consectetuer adipiscing elit, sed diam nonummy nibh euismod tincidunt ut laoreet dolore magna aliquam erat volutpat. Ut wisi enim ad minim veniam, quis nostrud exerci tation</p></div>
  <div class="abs" style="left:85px;top:96px;width:45px"><p class="name">Name Here</p><p class="small" style="font-size:3.2px;text-align:justify">Lorem ipsum dolor sit amet, consectetuer adipiscing elit, sed diam nonummy nibh euismod tincidunt ut laoreet dolore magna aliquam erat volutpat. Ut wisi enim ad minim veniam, quis nostrud exerci tation</p></div>
  <div class="abs" style="left:148px;top:96px;width:45px"><p class="name">Name Here</p><p class="small" style="font-size:3.2px;text-align:justify">Lorem ipsum dolor sit amet, consectetuer adipiscing elit, sed diam nonummy nibh euismod tincidunt ut laoreet dolore magna aliquam erat volutpat. Ut wisi enim ad minim veniam, quis nostrud exerci tation</p></div>
  <div class="abs" style="left:210px;top:96px;width:45px"><p class="name">Name Here</p><p class="small" style="font-size:3.2px;text-align:justify">Lorem ipsum dolor sit amet, consectetuer adipiscing elit, sed diam nonummy nibh euismod tincidunt ut laoreet dolore magna aliquam erat volutpat. Ut wisi enim ad minim veniam, quis nostrud exerci tation</p></div>
  <div class="abs brand brand-foot">PARTWISE<br>HELM</div>
</section>

<!-- Closing slide -->
<section class="slide dark col-r row-5">
  <svg class="shape" viewBox="0 0 278 173">
    <defs><linearGradient id="photoOrange2" x1="0" y1="0" x2="1" y2="1"><stop offset="0" stop-color="#d98a4e"/><stop offset=".6" stop-color="#9a5a33"/><stop offset="1" stop-color="#c77a45"/></linearGradient></defs>
    <path d="M133,0 C122,40 142,60 138,78 C128,112 150,148 180,155" fill="none" stroke="var(--orange)" stroke-width=".8"/>
    <path role="img" aria-label="Photo of a smiling executive presenting in a meeting room" d="M140,0 C130,40 150,60 145,78 C135,112 160,150 200,173 L278,173 L278,0 Z" fill="url(#photoOrange2)"/>
  </svg>
  <div class="abs brand brand-lg" style="left:19px">PARTWISE<br>HELM</div>
  <h2 class="abs thanks">Thank<br><span class="accent">You!</span></h2>
  <div class="abs contact"><p>www.partwisehelm.tech</p><p>+44 7700 900123</p><p>Mara Quill</p></div>
</section>

</main>
</body>
</html>
```